Orbit 528 - Pagevo Book Cover

I am looking for a Pagevo book cover for my book about "Orbit 528".
The Book is Titled:
Orbit 528 Advanced
Shaping Tomorrow: Paths Toward Unlocking Hidden Cosmic Laws
Author is Dorian Welby
Here is a book description that may help you understand more about it:
Inspired by the genius of Anton Brevik, this comprehensive guide delves into the ancient wisdom and cutting-edge science behind the 369 method, a powerful tool for manifesting your desires. Whether you're seeking personal growth, financial success, or spiritual enlightenment, this book provides advanced techniques and methods to transform your dreams into reality.
Any questions please ask.
Thanks
Colin

```html
<!DOCTYPE html>
<html lang="en">
<head>
<meta charset="utf-8">
<title>Orbit 528 Advanced — Dorian Welby</title>
<link href="https://fonts.googleapis.com/css2?family=Poppins:wght@400;700;900&family=Sacramento&display=swap" rel="stylesheet">
<style>
  :root {
    --paper: #ffffff;
    --navy: #1a5192;
    --cyan: #12c8ef;
    --ink: #111111;
    --glow-light: #cfe0f2;
    --glow-mid: #7fa6d2;
  }
  html, body {
    margin: 0;
    padding: 0;
    overflow: hidden;
    background: var(--paper);
  }
  .cover {
    position: relative;
    width: 750px;
    height: 1200px;
    background: var(--paper);
    overflow: hidden;
    font-family: 'Poppins', sans-serif;
  }
  .cover-art {
    position: absolute;
    left: 130px;
    top: 30px;
    width: 500px;
    height: 710px;
  }
  .series-label {
    position: absolute;
    left: 62px;
    top: 606px;
    margin: 0;
    font-weight: 700;
    font-size: 60px;
    line-height: 1;
    color: var(--cyan);
    letter-spacing: -0.5px;
  }
  .series-number {
    position: absolute;
    left: 100px;
    top: 640px;
    width: 600px;
    margin: 0;
    font-weight: 900;
    font-size: 330px;
    line-height: 1;
    color: var(--navy);
    text-align: center;
    letter-spacing: -10px;
  }
  .edition-script {
    position: absolute;
    left: 44px;
    top: 832px;
    width: 640px;
    margin: 0;
    font-family: 'Sacramento', cursive;
    font-size: 166px;
    font-weight: 400;
    line-height: 1;
    color: var(--cyan);
    text-align: center;
    white-space: nowrap;
  }
  .subtitle {
    position: absolute;
    left: 0;
    top: 1005px;
    width: 750px;
    margin: 0;
    font-weight: 400;
    font-size: 20px;
    line-height: 30px;
    color: var(--ink);
    text-align: center;
  }
  .author {
    position: absolute;
    left: 0;
    top: 1094px;
    width: 750px;
    margin: 0;
    font-weight: 700;
    font-size: 62px;
    line-height: 1.2;
    color: var(--navy);
    text-align: center;
    letter-spacing: 0.2em;
    text-indent: 0.2em;
    white-space: nowrap;
  }
</style>
</head>
<body>
  <main class="cover">
    <svg class="cover-art" viewBox="0 0 500 710" role="img" aria-label="Illustration: a branching blue neuron network radiating from a glowing core, with a silhouetted figure leaping up to touch its centre">
      <defs>
        <radialGradient id="networkGlow" cx="50%" cy="50%" r="50%">
          <stop offset="0%" stop-color="var(--navy)"/>
          <stop offset="14%" stop-color="var(--glow-mid)"/>
          <stop offset="40%" stop-color="var(--glow-light)"/>
          <stop offset="100%" stop-color="var(--paper)"/>
        </radialGradient>
      </defs>
      <circle cx="246" cy="242" r="242" fill="url(#networkGlow)"/>
    </svg>

    <h1 class="series-label">Orbit</h1>
    <p class="series-number">528</p>
    <p class="edition-script">Advanced</p>

    <h2 class="subtitle">Shaping Tomorrow:<br>Paths Toward Unlocking Hidden Cosmic Laws</h2>

    <p class="author">DORIAN WELBY</p>
  </main>
</body>
</html>
```